Design a Professional Business Card for Velmora Arcs

Design a business card for Velmora Arcs, we are a National Sport Court Company.

West Region Address: 4175 Quill Harbor Ln, Suite #215 Englewood, Colorado 80467
East Region Address: 3817 Tamsin Rd E, Bradenton, Florida 34583

Target Market(s)

High End Residential & Institutional Clients

Industry/Entity Type

Design & Construction

Contact Information for Business Card

Logo/Brand/Colors/ name, number (provided in comments)

Requirements
Must have
• Colors only provided in logo
Should not have
• Any other colors not in existing logo (attached)

```html
<!DOCTYPE html>
<html lang="en">
<head>
<meta charset="utf-8">
<title>Velmora Arcs — Business Card</title>
<link href="https://fonts.googleapis.com/css2?family=Arimo:wght@400;700&family=Oswald:wght@700&display=swap" rel="stylesheet">
<style>
  :root {
    --stage: #1f1f1f;
    --brand-green: #136b37;
    --brand-navy: #1c3566;
    --paper: #ffffff;
    --soft-circle: #eef1f4;
  }
  html, body {
    margin: 0;
    padding: 0;
    width: 1200px;
    height: 977px;
    overflow: hidden;
    background: var(--stage);
    font-family: "Arimo", Arial, sans-serif;
  }
  .canvas {
    position: relative;
    width: 1200px;
    height: 977px;
  }
  .card {
    position: absolute;
    width: 540px;
    height: 310px;
    border-radius: 18px;
    overflow: hidden;
  }

  /* Back side */
  .card-back {
    left: 80px;
    top: 130px;
    background: var(--brand-green);
    color: var(--paper);
  }
  .wordmark {
    position: absolute;
    display: flex;
    align-items: center;
    gap: 16px;
    font-weight: 700;
    text-transform: uppercase;
  }
  .wordmark-dot {
    border-radius: 50%;
    flex: none;
  }
  .card-back .wordmark {
    left: 120px;
    top: 88px;
    font-size: 46px;
    letter-spacing: 3px;
    color: var(--paper);
  }
  .card-back .wordmark-dot {
    width: 64px;
    height: 64px;
    background: var(--paper);
  }
  .regions {
    position: absolute;
    left: 40px;
    bottom: 36px;
    font-size: 13px;
    line-height: 22px;
  }
  .region {
    display: flex;
    align-items: center;
    gap: 6px;
    white-space: nowrap;
  }
  .region strong { font-weight: 700; }
  .icon { width: 12px; height: 12px; flex: none; }

  /* Front side */
  .card-front {
    left: 580px;
    top: 540px;
    background: var(--brand-navy);
    color: var(--paper);
  }
  .front-white {
    position: absolute;
    right: 0;
    top: 0;
    width: 140px;
    height: 100%;
    background: var(--paper);
  }
  .front-circle {
    position: absolute;
    left: 305px;
    top: -20px;
    width: 340px;
    height: 340px;
    border-radius: 50%;
    background: var(--paper);
  }
  .front-halo {
    position: absolute;
    left: 327px;
    top: 2px;
    width: 296px;
    height: 296px;
    border-radius: 50%;
    background: var(--soft-circle);
  }
  .card-front .wordmark {
    left: 348px;
    top: 126px;
    gap: 10px;
    font-size: 24px;
    line-height: 27px;
    letter-spacing: 1.5px;
    color: var(--brand-navy);
  }
  .card-front .wordmark-dot {
    width: 40px;
    height: 40px;
    background: var(--brand-green);
  }
  .contact {
    position: absolute;
    left: 36px;
    top: 150px;
    width: 255px;
  }
  .contact-name {
    font-family: "Oswald", "Arial Narrow", sans-serif;
    font-weight: 700;
    font-size: 21px;
    line-height: 26px;
    margin: 0;
    white-space: nowrap;
  }
  .contact-title {
    font-size: 14px;
    margin: 2px 0 10px;
  }
  .contact-list {
    list-style: none;
    margin: 0;
    padding: 0 0 0 20px;
    font-size: 13px;
    line-height: 19px;
  }
  .contact-list li {
    display: flex;
    align-items: center;
    gap: 8px;
    white-space: nowrap;
  }
</style>
</head>
<body>
<main class="canvas">

  <section class="card card-back" aria-label="Card back">
    <div class="wordmark">
      <span class="wordmark-dot"></span>
      <span>Velmora Arcs</span>
    </div>
    <div class="regions">
      <div class="region">
        <svg class="icon" viewBox="0 0 12 12"><path d="M6 0.5a3.8 3.8 0 0 0-3.8 3.8C2.2 7.2 6 11.5 6 11.5s3.8-4.3 3.8-7.2A3.8 3.8 0 0 0 6 0.5z" fill="#fff"/><circle cx="6" cy="4.3" r="1.4" fill="#136b37"/></svg>
        <span><strong>East Region</strong>: 3817 Tamsin Rd E, Bradenton, Florida 34583</span>
      </div>
      <div class="region">
        <svg class="icon" viewBox="0 0 12 12"><path d="M6 0.5a3.8 3.8 0 0 0-3.8 3.8C2.2 7.2 6 11.5 6 11.5s3.8-4.3 3.8-7.2A3.8 3.8 0 0 0 6 0.5z" fill="#fff"/><circle cx="6" cy="4.3" r="1.4" fill="#136b37"/></svg>
        <span><strong>West Region</strong>: 4175 Quill Harbor Ln, Suite #215 Englewood, Colorado 80467</span>
      </div>
    </div>
  </section>

  <section class="card card-front" aria-label="Card front">
    <div class="front-white"></div>
    <div class="front-circle"></div>
    <div class="front-halo"></div>
    <div class="wordmark">
      <span class="wordmark-dot"></span>
      <span>Velmora<br>Arcs</span>
    </div>
    <div class="contact">
      <h1 class="contact-name">Dorian L. Whitcombe, ASLA</h1>
      <p class="contact-title">CEO &amp; Founder</p>
      <ul class="contact-list">
        <li>
          <svg class="icon" viewBox="0 0 12 12"><path d="M3 1l2 2.4-1.1 1.3a7 7 0 0 0 3.4 3.4L8.6 7 11 9l-1.4 2C5 11 1 7 1 2.4z" fill="#fff"/></svg>
          <span>(303) 555-0147 (Direct)</span>
        </li>
        <li>
          <svg class="icon" viewBox="0 0 12 12"><path d="M3 1l2 2.4-1.1 1.3a7 7 0 0 0 3.4 3.4L8.6 7 11 9l-1.4 2C5 11 1 7 1 2.4z" fill="#fff"/></svg>
          <span>1-800-555-0193 (Main)</span>
        </li>
        <li>
          <svg class="icon" viewBox="0 0 12 12"><rect x="0.5" y="2.5" width="11" height="7" fill="#fff"/><path d="M0.5 2.5L6 6.5l5.5-4" fill="none" stroke="#1c3566" stroke-width="1"/></svg>
          <span>dorian@velmoraco.com</span>
        </li>
        <li>
          <svg class="icon" viewBox="0 0 12 12"><circle cx="6" cy="6" r="5.3" fill="#fff"/><path d="M0.7 6h10.6M6 0.7c-2.4 3-2.4 7.6 0 10.6M6 0.7c2.4 3 2.4 7.6 0 10.6" fill="none" stroke="#1c3566" stroke-width="0.9"/></svg>
          <span>velmoraarcs.com</span>
        </li>
      </ul>
    </div>
  </section>

</main>
</body>
</html>
```